Mexican construction company needs a business card design

We need a business card design for a company based in Monterrey, Mexico called:

Desarrollos Tolvani S.A. de C.V.

The company is in the construction business and I would like the businees card to be simple and concise. Please use white background and blue or black text color that say:

"Proyectos de Construcción"-- (Brief description of business)
" Rodrigo Ulloa Benítez"--- (My name)
"rulloab@correovelo.mx"-- (My email)
"C: (81) 82 19 57 46"-- (My cell)
"O: (81) 86 72 13 95"-- (Office phone)

Please use only the colors of my company that are attached

Please make the back of the business card blue (same blue from logo) and use the logo.

Thanks!

```html
<!DOCTYPE html>
<html lang="es">
<head>
<meta charset="utf-8">
<title>Desarrollos Tolvani — Tarjeta de presentación</title>
<link rel="stylesheet" href="https://fonts.googleapis.com/css2?family=Open+Sans:wght@400;600&display=swap">
<style>
  :root {
    --backdrop: #e9e7e4;
    --card: #ffffff;
    --navy: #1d1a45;
    --ink: #3b3c55;
    --silver-light: #d9dadf;
    --silver-dark: #6f7079;
    --sand: #d9c8a4;
  }
  * { margin: 0; padding: 0; box-sizing: border-box; }
  html, body {
    width: 1200px;
    height: 970px;
    overflow: hidden;
    background: var(--backdrop);
    font-family: "Open Sans", Arial, sans-serif;
  }
  .business-card {
    position: absolute;
    left: 80px;
    top: 196px;
    width: 1040px;
    height: 578px;
    background: var(--card);
    overflow: hidden;
    box-shadow: 0 10px 30px rgba(0,0,0,0.12);
  }
  .card-waves {
    position: absolute;
    inset: 0;
    width: 1040px;
    height: 578px;
  }
  .brand {
    position: absolute;
    left: 69px;
    top: 86px;
    display: flex;
    align-items: center;
    gap: 34px;
  }
  .brand-square {
    width: 150px;
    height: 150px;
    background: var(--navy);
  }
  .brand-name {
    color: var(--navy);
    font-weight: 600;
    text-transform: uppercase;
    line-height: 1;
  }
  .brand-name .line-top {
    display: block;
    font-size: 36px;
    letter-spacing: 3px;
  }
  .brand-name .line-main {
    display: block;
    font-size: 66px;
    letter-spacing: 4px;
    margin-top: 8px;
  }
  .tagline {
    position: absolute;
    left: 67px;
    top: 326px;
    font-size: 24px;
    color: var(--ink);
  }
  .person-name {
    position: absolute;
    left: 67px;
    top: 376px;
    font-size: 28px;
    font-weight: 600;
    color: var(--ink);
  }
  .contact-list {
    position: absolute;
    right: 52px;
    top: 416px;
    list-style: none;
    color: var(--sand);
    font-size: 22px;
  }
  .contact-list li {
    display: flex;
    justify-content: flex-end;
    align-items: center;
    gap: 18px;
    height: 36.5px;
  }
  .contact-list svg {
    width: 26px;
    height: 22px;
    fill: none;
    stroke: var(--sand);
    stroke-width: 1.8;
  }
</style>
</head>
<body>
  <div class="business-card">
    <svg class="card-waves" viewBox="0 0 1040 578" aria-hidden="true">
      <defs>
        <linearGradient id="silver" x1="0" y1="0" x2="1" y2="0">
          <stop offset="0" stop-color="var(--silver-light)"/>
          <stop offset="0.45" stop-color="var(--silver-dark)"/>
          <stop offset="1" stop-color="var(--silver-light)"/>
        </linearGradient>
      </defs>
      <path d="M0,452 C160,492 340,500 520,420 C700,338 860,268 1040,250 L1040,272 C860,290 700,352 520,448 C340,540 150,536 0,522 Z" fill="url(#silver)"/>
      <path d="M100,472 C300,505 420,475 560,410" fill="none" stroke="var(--silver-light)" stroke-width="3"/>
      <path d="M0,578 L0,536 C200,552 360,540 530,452 C710,356 860,294 1040,278 L1040,578 Z" fill="var(--navy)"/>
    </svg>

    <div class="brand">
      <div class="brand-square"></div>
      <div class="brand-name">
        <span class="line-top">Desarrollos</span>
        <span class="line-main">Tolvani</span>
      </div>
    </div>

    <p class="tagline">Proyectos de Construcción</p>
    <p class="person-name">Rodrigo Ulloa Benítez</p>

    <ul class="contact-list">
      <li>(81) 86 72 13 95
        <svg viewBox="0 0 26 22" aria-label="Teléfono de oficina" role="img"><path d="M3 8 Q13 1 23 8 L21 11 L17 9 L17 7 Q13 5 9 7 L9 9 L5 11 Z"/><rect x="6" y="12" width="14" height="8" rx="1"/></svg>
      </li>
      <li>(81) 82 19 57 46
        <svg viewBox="0 0 26 22" aria-label="Celular" role="img"><rect x="8" y="1" width="10" height="20" rx="2"/><line x1="11" y1="18" x2="15" y2="18"/></svg>
      </li>
      <li>rulloab@correovelo.mx
        <svg viewBox="0 0 26 22" aria-label="Correo electrónico" role="img"><rect x="2" y="4" width="22" height="14"/><path d="M2 4 L13 12 L24 4"/></svg>
      </li>
    </ul>
  </div>
</body>
</html>
```